Bathroom Renovation Business card design needed

Bathroom, Kitchen & Laundry Renovations
Mainly complete bathroom renovations

Target Market(s)

people wanting a total bathroom renovations and other trades people

Industry/Entity Type

Business

Contact Information for Business Card

Dalby Bathrooms
Tomas Dalby
Mobile: 0438 207615
Licence no: 764519K
Email: dalbybathrooms@mailnest.example

Logo styles of interest
Lettermark Logo
Requirements
Must have
• the business card should be predominantly blue
Nice to have
• the DB logo featured in the business card will be used on tshirts,tax invoices , letters etc so the DB will be the main feature, and preferably blue
Should not have
• We found the red DB logo through google images. We understand that it cannot be exactly the same but we like how the DB is linked. The example business card is something we designed but we prefer more blues. Maybe different shades of blue.

```html
<!DOCTYPE html>
<html lang="en">
<head>
<meta charset="utf-8">
<title>Dalby Bathrooms – Business Card</title>
<link rel="stylesheet" href="https://fonts.googleapis.com/css2?family=Roboto:wght@300;400&family=Roboto+Condensed:wght@700&display=swap">
<style>
  :root {
    --backdrop: #2b2c2e;
    --card-blue: #1b64a1;
    --card-blue-deep: #175893;
    --strip-light: #9fbfe0;
    --strip-mid: #4f86bf;
    --panel-white: #f7f7f7;
    --accent-blue: #3b9bd8;
    --label-blue: #3d92cf;
    --detail-grey: #555a60;
    --icon-grey: #8a8f95;
    --white: #ffffff;
  }
  * { box-sizing: border-box; margin: 0; padding: 0; }
  html, body {
    width: 1200px;
    height: 750px;
    overflow: hidden;
    background: var(--backdrop);
  }
  .stage {
    position: relative;
    width: 1200px;
    height: 750px;
  }
  .business-card {
    position: absolute;
    left: 100px;
    top: 95px;
    width: 1000px;
    height: 560px;
    background: var(--card-blue);
    overflow: hidden;
    font-family: "Roboto", Arial, sans-serif;
  }
  .card-strip {
    position: absolute;
    left: 0;
    bottom: 0;
    width: 100%;
    height: 92px;
    background: linear-gradient(100deg, var(--card-blue-deep) 0%, var(--strip-mid) 45%, var(--strip-light) 100%);
  }
  .card-strip::before {
    content: "";
    position: absolute;
    left: 0; top: 0;
    width: 100%; height: 3px;
    background: rgba(255,255,255,0.35);
  }
  .contact-panel {
    position: absolute;
    left: 652px;
    top: 0;
    width: 348px;
    height: 468px;
  }
  .contact-panel svg.panel-shape {
    position: absolute;
    inset: 0;
  }
  .contact-name {
    position: absolute;
    left: 34px;
    top: 58px;
    font-weight: 300;
    font-size: 48px;
    color: var(--accent-blue);
    white-space: nowrap;
  }
  .contact-item {
    position: absolute;
    left: 34px;
    width: 300px;
  }
  .contact-label {
    display: block;
    margin-left: 78px;
    font-family: "Roboto Condensed", "Arial Narrow", sans-serif;
    font-weight: 700;
    font-size: 21px;
    color: var(--label-blue);
  }
  .contact-value {
    display: block;
    margin-left: 68px;
    margin-top: 2px;
    font-size: 14px;
    color: var(--detail-grey);
    white-space: nowrap;
  }
  .contact-icon {
    position: absolute;
    left: 10px;
    top: 26px;
  }
  .contact-item--email { top: 160px; }
  .contact-item--mobile { top: 250px; }
  .contact-item--licence { top: 340px; }
  .licence-prefix {
    position: absolute;
    left: 4px;
    top: 28px;
    font-style: italic;
    font-size: 22px;
    color: var(--detail-grey);
  }
  .brand-line {
    position: absolute;
    left: 0;
    top: 330px;
    display: flex;
    align-items: center;
    gap: 26px;
  }
  .brand-square {
    width: 108px;
    height: 56px;
    background: var(--white);
  }
  .brand-name {
    font-weight: 300;
    font-size: 58px;
    color: var(--white);
    white-space: nowrap;
    letter-spacing: 0.5px;
  }
</style>
</head>
<body>
<main class="stage">
  <section class="business-card" aria-label="Dalby Bathrooms business card">
    <div class="card-strip"></div>

    <div class="brand-line">
      <span class="brand-square"></span>
      <span class="brand-name">Dalby Bathrooms</span>
    </div>

    <div class="contact-panel">
      <svg class="panel-shape" width="348" height="468" viewBox="0 0 348 468" aria-hidden="true">
        <path d="M0 40 Q150 12 348 0 L348 468 L0 468 Z" fill="var(--panel-white)"/>
      </svg>

      <h1 class="contact-name">Tomas Dalby</h1>

      <div class="contact-item contact-item--email">
        <svg class="contact-icon" width="34" height="24" viewBox="0 0 34 24" aria-hidden="true">
          <rect x="1" y="1" width="32" height="22" fill="none" stroke="var(--icon-grey)" stroke-width="1.5"/>
          <polyline points="1,1 17,14 33,1" fill="none" stroke="var(--icon-grey)" stroke-width="1.5"/>
        </svg>
        <span class="contact-label">Email</span>
        <span class="contact-value">dalbybathrooms@mailnest.example</span>
      </div>

      <div class="contact-item contact-item--mobile">
        <svg class="contact-icon" width="16" height="26" viewBox="0 0 16 26" aria-hidden="true">
          <rect x="1" y="1" width="14" height="24" rx="2" fill="none" stroke="var(--icon-grey)" stroke-width="1.5"/>
          <rect x="4" y="4" width="8" height="13" fill="var(--icon-grey)"/>
          <circle cx="8" cy="21" r="1.5" fill="var(--icon-grey)"/>
        </svg>
        <span class="contact-label">Mobile</span>
        <span class="contact-value">0438 207615</span>
      </div>

      <div class="contact-item contact-item--licence">
        <span class="licence-prefix">no:</span>
        <span class="contact-label">Licence</span>
        <span class="contact-value">764519K</span>
      </div>
    </div>
  </section>
</main>
</body>
</html>
```